conférence Débat Innovation
Bonjour,
Dans le cadre de l'organisation d'un événement institutionnel, je suis à la recherche d'un professionnel graphiste pour la création des supports suivants :
- flyer de l'événement (pour web et print),
- version pour les réseaux sociaux et le site internet de l'événement,
- flyer de cet événement personnalisé pour un concours dont la finale aura lieu le jour de l'événement,
- version affiches pour le jour J,
- Carton d'invitation pour mailing et impression.
L'événement est une conférence débat sur l'entreprenariat et l'innovation en banlieue parisienne.
L'idée est de dynamiser un territoire et le mettre en avant ses atouts.

```html
<!DOCTYPE html>
<html lang="fr">
<head>
<meta charset="utf-8">
<title>L'entreprenariat et l'innovation en banlieue parisienne</title>
<link rel="stylesheet" href="https://fonts.googleapis.com/css2?family=Exo+2:wght@400;500;600&display=swap">
<style>
  :root {
    --blue-deep: #0f2f5c;
    --blue-mid: #1d5592;
    --blue-light: #3f7fc0;
    --orange: #f59b2f;
    --white: #ffffff;
    --font: "Exo 2", sans-serif;
  }
  * { margin: 0; padding: 0; box-sizing: border-box; }
  html, body { width: 1200px; height: 850px; overflow: hidden; background: var(--blue-deep); }
  .poster {
    position: relative; width: 1200px; height: 850px; overflow: hidden;
    font-family: var(--font); color: var(--white);
  }
  .backdrop-photo {
    position: absolute; inset: 0;
    background:
      radial-gradient(ellipse at 30% 55%, rgba(63,127,192,.55), transparent 60%),
      linear-gradient(135deg, var(--blue-mid) 0%, #174a82 45%, var(--blue-deep) 100%);
  }
  .bulb-motif {
    position: absolute; left: 130px; top: 40px; width: 880px; height: 780px;
    border-radius: 50% 50% 42% 42%;
    background: radial-gradient(ellipse at 50% 40%, rgba(255,255,255,.10), rgba(255,255,255,0) 70%);
  }
  .corner-motif {
    position: absolute; right: 40px; top: 20px; width: 200px; height: 160px;
    border-radius: 50%;
    background: radial-gradient(circle, rgba(120,170,220,.35), rgba(120,170,220,0) 70%);
  }
  .territory-visual {
    position: absolute; left: 490px; top: 250px; width: 530px; height: 470px;
    border: 4px solid var(--white);
    border-radius: 42% 38% 44% 36%;
    background: linear-gradient(160deg, #8fb6dc 0%, #4b7fb8 50%, #1f4e86 100%);
    box-shadow: 0 0 30px rgba(255,255,255,.35);
  }
  .hatch-mark {
    position: absolute; left: 22px; top: 700px; width: 80px; height: 80px;
    background: var(--orange); transform: rotate(-15deg);
  }
  .title {
    position: absolute; left: 68px; top: 22px;
    color: var(--orange); font-weight: 500; line-height: 1.05;
  }
  .title .line-1 { display: block; font-size: 66px; }
  .title .line-2 { display: block; font-size: 62px; margin-left: 46px; }
  .subtitle {
    position: absolute; left: 355px; top: 195px; font-size: 23px; font-weight: 500;
  }
  .format {
    position: absolute; left: 92px; top: 360px;
    color: var(--orange); font-size: 23px; line-height: 1.15; font-weight: 500;
  }
  .date {
    position: absolute; left: 68px; top: 448px; font-size: 50px; font-weight: 600;
  }
  .time {
    position: absolute; left: 120px; top: 512px; font-size: 23px; font-weight: 500;
  }
  .venue {
    position: absolute; left: 118px; top: 560px;
    color: var(--orange); font-size: 29px; font-weight: 500; line-height: 1.3;
  }
  .venue .city { display: block; margin-left: 106px; }
  .footer {
    position: absolute; left: 150px; top: 798px; font-size: 21px; font-weight: 500;
  }
  .footer .phone { margin-left: 50px; }
  .contest-badge {
    position: absolute; left: 990px; top: 648px; width: 175px; height: 180px;
    background: var(--white); transform: rotate(-12deg);
    display: flex; align-items: center; justify-content: center; text-align: center;
  }
  .contest-badge span {
    color: var(--orange); font-size: 27px; font-weight: 600; line-height: 1.1;
  }
</style>
</head>
<body>
<div class="poster">
  <div class="backdrop-photo" role="img" aria-label="Photo teintée en bleu de jeunes entrepreneurs travaillant ensemble"></div>
  <div class="bulb-motif" role="img" aria-label="Grande ampoule en filigrane, symbole de l'innovation"></div>
  <div class="corner-motif" role="img" aria-label="Motif de réseau de points reliés"></div>
  <div class="territory-visual" role="img" aria-label="Carte de l'Île-de-France contenant une photo de coureuses devant des immeubles"></div>
  <div class="hatch-mark" role="img" aria-label="Motif graphique orange quadrillé"></div>

  <h1 class="title">
    <span class="line-1">L’entreprenariat</span>
    <span class="line-2">et l’innovation</span>
  </h1>
  <p class="subtitle">en banlieue parisienne</p>

  <p class="format">Débat / Conférence<br>Ouvert à tous</p>
  <p class="date">21 sept. 2016</p>
  <p class="time">àpartir de 10h30</p>
  <p class="venue">Palais des rencontres<span class="city">Paris</span></p>

  <p class="footer">
    <span class="website">www.concoursjeunespousses2016.fr</span>
    <span class="phone">01 00 04 00 05</span>
  </p>

  <div class="contest-badge"><span>Concours<br>Start UP<br>2016</span></div>
</div>
</body>
</html>
```